Hip, Modern Home Page for Successful SEO Expert

Marcus Delwyn is an SEO expert, author and professional speaker. His site is
www.marcusdelwyn.net. We need a re-design of the website so that it does not look outdated or like an off-the-shelf Wordpress template (like it currently does). The new design must convey to the visitor a compelling call-to-action. Specially, this home page will act as a “squeeze page” and thus, the primary marketing goal will be to get the user to opt in to our list. The new design will provide elements of “social proof” such as written testimonials, a portfolio of case studies, client logos, “as appeared on” logos, client testimonial video, etc.
Updates

Please incorporate the recently uploaded headshots into your design 

Target Market(s)

People looking for help in internet marketing for their websites, entrepreneurs, start-ups, bloggers, companies looking to build an online presence, conferences looking to book Marcus for speaking. Small business people and SEO newbies interested in buying Marcus’s video-based training (RankCraftLab.net).

Industry/Entity Type

Marketing

Font styles to use
Sans Serif

Colors
f68d4d
3276b5
8769ae
acd036

Requirements
Must have
• strong call to action
Should not have
• should not look like a template. should not use old style fonts. should not have more than one page scroll

```html
<!DOCTYPE html>
<html lang="en">
<head>
<meta charset="utf-8">
<title>Marcus Delwyn — SEO Expert, Author, Professional Speaker</title>
<link href="https://fonts.googleapis.com/css2?family=Bebas+Neue&family=Lato:wght@400;700&display=swap" rel="stylesheet">
<style>
  :root {
    --orange: #f68d4d;
    --blue: #3276b5;
    --purple: #8769ae;
    --lime: #acd036;
    --charcoal: #333333;
    --footer: #2a2a2a;
    --card: #e4e4e4;
    --teal: #2a9a9a;
    --ink: #222222;
    --muted: #9a9a9a;
    --white: #ffffff;
  }
  * { box-sizing: border-box; margin: 0; padding: 0; }
  html, body { width: 1143px; height: 1200px; overflow: hidden; background: var(--charcoal); }
  body { position: relative; font-family: "Lato", sans-serif; color: var(--ink); }

  .hero { position: absolute; left: 0; top: 0; width: 1143px; height: 597px; overflow: hidden; }
  .hero-photo {
    position: absolute; inset: 0;
    background:
      radial-gradient(ellipse 260px 330px at 250px 300px, #6f7b8c 0%, #8a8f99 45%, rgba(200,205,210,0) 100%),
      linear-gradient(180deg, #c9cfc9 0%, #eef0f0 18%, #f4f5f5 60%, #e9ecee 100%);
  }
  .name-band { position: absolute; left: 0; top: 487px; width: 1143px; height: 110px; background: rgba(240,240,240,0.72); }
  .hero-name {
    position: absolute; left: 114px; top: 494px;
    font-family: "Bebas Neue", sans-serif; font-size: 72px; line-height: 1; color: #262626; letter-spacing: 0.5px;
  }
  .hero-role { position: absolute; left: 108px; top: 561px; font-size: 23px; color: #262626; }

  .main-nav { position: absolute; right: 54px; top: 36px; display: flex; gap: 34px; }
  .main-nav a {
    font-family: "Bebas Neue", sans-serif; font-size: 29px; color: var(--white); text-decoration: none;
    text-shadow: 0 1px 2px rgba(0,0,0,0.55);
  }

  .optin {
    position: absolute; left: 678px; top: 147px; width: 372px; height: 450px;
    background: var(--charcoal); border-radius: 6px 6px 0 0; text-align: center; color: var(--white);
  }
  .optin h2 { margin: 50px 30px 0; font-size: 28px; line-height: 34px; font-weight: 700; }
  .optin p { margin: 12px 34px 0; font-size: 17.5px; line-height: 23px; }
  .optin input {
    display: block; margin: 22px auto 0; width: 298px; height: 50px; border: 1px solid #bdbdbd; border-radius: 3px;
    background: #f4f4f4; padding: 0 10px; font: 18px "Lato", sans-serif; color: #777;
  }
  .optin button {
    display: block; margin: 26px auto 0; width: 246px; height: 52px; border: 0; background: var(--lime);
    font: 20px "Lato", sans-serif; color: #2b2b2b;
  }

  .testimonial { position: absolute; left: 0; top: 624px; width: 1143px; text-align: center; color: var(--white); }
  .testimonial blockquote { font-family: "Bebas Neue", sans-serif; font-size: 31px; line-height: 34px; letter-spacing: 0.3px; }
  .testimonial cite {
    display: block; width: 1005px; text-align: right; font-family: "Bebas Neue", sans-serif; font-style: italic;
    font-size: 24px; color: #c8c8c8; margin-top: 2px;
  }

  .features { position: absolute; left: 0; top: 751px; width: 1143px; }
  .feature { position: absolute; top: 0; width: 308px; }
  .feature-head {
    height: 58px; color: var(--white); text-align: center; font-family: "Bebas Neue", sans-serif; font-size: 38px;
    line-height: 62px; border-bottom: 4px solid rgba(0,0,0,0.18);
  }
  .feature-body { margin: 0 8px; background: var(--card); height: 246px; padding: 14px 26px 0; }
  .feature-body p { font-size: 18.5px; line-height: 23px; color: #222; }
  .feature-body a { font-size: 19.5px; color: var(--teal); text-decoration: none; line-height: 24px; }
  .feature-media { margin-top: 16px; width: 256px; height: 104px; border: 3px solid var(--white); }
  .speaking { left: 88px; }  .speaking .feature-head { background: var(--orange); }
  .books { left: 419px; }    .books .feature-head { background: var(--blue); }
  .blog { left: 747px; }     .blog .feature-head { background: var(--purple); }
  .speaking .feature-media { background: linear-gradient(135deg, #b07a45, #d7a670 55%, #8e6036); }
  .books .feature-media { background: linear-gradient(90deg, #2c7a2e, #56a83c 55%, #8cca3f); }
  .blog .feature-media { background: linear-gradient(90deg, #e8e8e8, #9c8d86 50%, #4a4a4a); }

  .site-footer { position: absolute; left: 0; top: 1095px; width: 1143px; height: 105px; background: var(--footer); text-align: center; }
  .footer-nav { display: flex; justify-content: center; gap: 30px; margin-top: 34px; }
  .footer-nav a { font-size: 15.5px; color: #c4c4c4; text-decoration: none; }
  .copyright { margin-top: 20px; font-size: 13px; color: var(--muted); }
</style>
</head>
<body>
  <header class="hero">
    <div class="hero-photo" role="img" aria-label="Portrait of Marcus Delwyn, arms crossed, in front of a soft waterfront backdrop"></div>
    <nav class="main-nav">
      <a href="#">About</a><a href="#">Blog</a><a href="#">Speaking</a><a href="#">Contact</a>
    </nav>
    <div class="name-band"></div>
    <h1 class="hero-name">Marcus Delwyn</h1>
    <p class="hero-role">SEO Expert, Author, Professional Speaker</p>
    <form class="optin">
      <h2>Learn how you can make $10,000/month Blogging 2 hours a day.</h2>
      <p>Lorem ipsum dolor sit amet, consectetur adipiscing elit. Integer aliquet lobortis purus. Pellentesque pellentesque eleifend leo.</p>
      <input type="email" placeholder="Your Email" aria-label="Your Email">
      <button type="button">Get It Now</button>
    </form>
  </header>

  <section class="testimonial">
    <blockquote>“Marcus Delwyn is the SEO master. Anyone who wants to know how SEO really<br>works must read The Ranking Playbook. This is a true reference work.”</blockquote>
    <cite>– Dale Renner, Superblogger dalerenner.com</cite>
  </section>

  <section class="features">
    <article class="feature speaking">
      <h3 class="feature-head">Speaking</h3>
      <div class="feature-body">
        <p>Lorem ipsum dolor sit amet, consectetur adipiscing elit. Vbulum quis fermentum</p>
        <a href="#">Learn More</a>
        <div class="feature-media" role="img" aria-label="Marcus speaking at a conference panel"></div>
      </div>
    </article>
    <article class="feature books">
      <h3 class="feature-head">Books</h3>
      <div class="feature-body">
        <p>Lorem ipsum dolor sit amet, consectetur adipiscing elit. Vbulum quis fermentum</p>
        <a href="#">Learn More</a>
        <div class="feature-media" role="img" aria-label="Cover of the book The Ranking Playbook"></div>
      </div>
    </article>
    <article class="feature blog">
      <h3 class="feature-head">Blog</h3>
      <div class="feature-body">
        <p>Lorem ipsum dolor sit amet, consectetur adipiscing elit. Vbulum quis fermentum</p>
        <a href="#">Learn More</a>
        <div class="feature-media" role="img" aria-label="Marcus chatting with attendees at an industry event"></div>
      </div>
    </article>
  </section>

  <footer class="site-footer">
    <nav class="footer-nav">
      <a href="#">ABOUT</a><a href="#">BOOKS</a><a href="#">SPEAKING</a><a href="#">INTERVIEWS</a><a href="#">TESTIMONIALS</a><a href="#">BLOG</a><a href="#">CONTACT</a>
    </nav>
    <p class="copyright">copyright © 2014 Marcus Delwyn. All rights reserved.</p>
  </footer>
</body>
</html>
```